Human Resources consulting firm website

I recently started a consulting firm after 30 years in Human Resources (Executive Development) work with Meridian 25 companies. I am looking for a website design that will convey both the services I provide (all in the HR / executive development arena) as well as sense of trust in me and my abilities (many years of experience, breadth of knowledge).

In the attachment section, there is a document with links to a number of websites fr firms that do similar work to me - the doc shares what I like about them and what I do not. I've also include my bio to give you a sens of who I am /what I do. The head shot will be replaced soon as I'm having new photos take, but the verbiage is what's important.

I need your help with the look and feel as well as different ideas on how to share the info. I am looking for your creativity and experience. I have not done a website for anything in the past.

Looking forward to working together on a great project and product!!

Target Market(s)

Any company looking for senior leader caoching, assessments of those leaders or help with a CEO transition. My wheelhouse is Meridian top 100 companies, but am able to work with small firms as well. Also any Board of Directors and upstarts in California.

Industry/Entity Type

Consulting

Coding

Coded - Design and coding required

Number of Pages Required

5+ page

Font styles to use
Sans Serif
Other font styles liked:
• Do not have a specific one but am very open to options

Colors

Designer to choose colors to be used in the design.

Requirements
Must have
• My project must have be professional (see the type of companies I am targeting) with an air of simplicity.
• A professional yet approachable look and feel that delivers:
• (1) I want there to be a landing page (with limited info - a more of a "teaser")
• (2) a tab for about us (with a few sentences about the company, my photo and option to link to my bio)
• (3) a tab for the services offered (one page with tiles that have a little bit about the services and the option to link to more info)
• (4) a tab to contact me (form to fill out with some personal info and the request that will get sent to my email).
• (5) diversity in the imagery
• (6) I plan for it to be mostly static. I will not be adding/changing regularly (although imagine the first couple months will want to tweak it as I get feedback). I do not plan to add blogs, etc.
Nice to have
• (1) Good graphics. I'm ok with black and white if it's classic or color photos. I don't want stalk photos anyone can get on the web. A sophisticated yet approachable look is what I'm going for.
• (2) Ability to get to know me (the principal) just a bit. That can be through the verbiage, colors, photos, etc.
• (3) Ability to contact me from the front home/landing page or contact page.
• (4) When someone looks me up on line, I want them to see a sentence or two about the company and have links that will take them straight to the page on the website they are looking for (contact, about us, etc.)
Should not have
• I do not want this to be:
• (1) overly feminine (not pink, purple, etc.),
• (2) flashy (I'm fine with a small video or moving photo but doubt I want anything beyond that) or
• (3) too close to the "out there" category (this is a professional business with corporate clients).
• (4) sterile (I'm selling myself .. that's what people buy when they hire a consultant).
• (5) basic - I do not want this to look like I hired my nephew straight out of college to build this. I'm looking for a strong, professional look.

```html
<!DOCTYPE html>
<html lang="en">
<head>
<meta charset="utf-8">
<title>Whitmore Talent Partners</title>
<link href="https://fonts.googleapis.com/css2?family=Michroma&family=Arimo:ital,wght@0,400;0,700;1,400;1,700&family=Open+Sans:wght@600&display=swap" rel="stylesheet">
<style>
:root{
  --blue:#7ea6d3;
  --blue-dark:#6b93c1;
  --grey-text:#6f6f6f;
  --heading:#666;
  --light-bg:#f7f7f7;
  --footer:#222;
  --white:#fff;
  --photo-dark:#5c5c5c;
  --photo-light:#b9b9b9;
}
*{margin:0;padding:0;box-sizing:border-box}
html,body{width:1200px;height:3049px;overflow:hidden;background:var(--white)}
body{font-family:"Arimo",Arial,sans-serif;color:var(--grey-text);position:relative}
.wrap{position:absolute;left:111px;width:978px}
.display{font-family:"Michroma",sans-serif;font-weight:400;letter-spacing:1px}
.accent{color:var(--blue)}
.btn{display:inline-block;background:var(--blue);color:var(--white);font-weight:700;font-size:14px;text-transform:uppercase;padding:0 17px;height:43px;line-height:43px;text-decoration:none}
.photo{background:linear-gradient(135deg,var(--photo-light),var(--photo-dark))}

/* top bar */
.topbar{position:absolute;top:0;left:0;width:1200px;height:41px;background:var(--blue);color:var(--white);font-size:14px}
.topbar .mail{position:absolute;left:111px;top:13px;display:flex;gap:8px;align-items:center}
.topbar .call{position:absolute;right:111px;top:11px;display:flex;gap:8px;align-items:center}
.topbar .call b{font-size:17px}

/* header */
.header{position:absolute;top:41px;left:0;width:1200px;height:108px}
.brand{position:absolute;left:111px;top:28px;display:flex;align-items:center;gap:12px}
.brand .mark{width:44px;height:44px;background:var(--blue)}
.brand .name{font-family:"Michroma",sans-serif;font-size:17px;line-height:21px;color:var(--blue);text-transform:uppercase}
.nav{position:absolute;left:417px;top:0;display:flex;height:108px;align-items:center;font-size:15px;font-weight:700;color:#222}
.nav a{color:inherit;text-decoration:none;margin-right:45px}
.nav a.active{color:var(--blue);background:linear-gradient(#e4edf7,#fff);padding:0 12px;height:80px;line-height:98px;margin-left:0;margin-right:33px;position:relative;top:-14px}
.login{position:absolute;right:111px;top:33px;width:109px;text-align:center}

/* hero */
.hero{position:absolute;top:149px;left:0;width:1200px;height:523px;background:linear-gradient(180deg,#9a9a9a,#4d4d4d)}
.hero h1{position:absolute;top:198px;width:100%;text-align:center;font-size:48px;line-height:54px;color:var(--white);letter-spacing:2px}
.hero .arrow{position:absolute;top:250px}

/* services */
.vline{position:absolute;left:600px;width:1px;background:#999}
.section-title{position:absolute;width:1200px;text-align:center;font-size:36px;color:var(--heading)}
.intro{position:absolute;left:240px;width:720px;text-align:center;font-size:14px;line-height:29px}
.service h3{font-family:"Open Sans",sans-serif;font-weight:600;font-size:25px;color:var(--heading);margin-bottom:14px}
.service p{font-size:14px;line-height:26px;margin-bottom:20px}
.service{position:absolute;width:438px}

/* about */
.about{position:absolute;top:1477px;left:0;width:1200px;height:529px;background:var(--light-bg)}
.about .text{position:absolute;left:111px;top:85px;height:357px;border-left:1px solid #999;padding-left:42px;width:540px}
.about h2{font-size:36px;line-height:48px;color:var(--heading);margin-bottom:22px}
.about p{font-size:14px;line-height:26px;text-align:justify;width:493px;margin-bottom:25px}
.about .photo{position:absolute;left:706px;top:85px;width:381px;height:357px;border:2px solid #ddd}

/* testimonial */
.testimonial{position:absolute;top:2092px;left:157px;width:886px;height:286px;border-top:1px solid #999}
.testimonial .photo{position:absolute;left:0;top:0;width:288px;height:286px}
.testimonial h2{position:absolute;left:318px;top:22px;font-size:34px;color:var(--heading)}
.quote{position:absolute;left:390px;top:112px;width:460px;font-style:italic;font-size:14px;line-height:29px}
.who{position:absolute;left:381px;top:208px;font-size:14px;font-style:italic;font-weight:700}
.role{position:absolute;left:390px;top:235px;font-size:12px}
.q-open{position:absolute;left:322px;top:100px}
.q-close{position:absolute;left:808px;top:200px}
.dots{position:absolute;top:2417px;left:576px;display:flex;gap:4px}
.dots span{width:13px;height:13px;border:1.5px solid #222;border-radius:50%}
.dots span.on{border-color:var(--blue);background:radial-gradient(var(--blue) 35%,transparent 40%)}

/* cta */
.cta{position:absolute;top:2514px;left:0;width:1200px;height:182px;background:var(--blue);text-align:center}
.cta h2{color:var(--white);font-size:21px;font-weight:700;margin-top:60px;letter-spacing:.3px}
.cta a{display:inline-block;margin-top:22px;background:var(--white);color:var(--blue);font-weight:700;font-size:14px;padding:0 20px;height:44px;line-height:44px;text-decoration:none}

/* footer */
.footer{position:absolute;top:2696px;left:0;width:1200px;height:353px;background:var(--footer);color:var(--white)}
.footer nav{position:absolute;top:70px;width:1200px;text-align:center;font-size:14px}
.footer nav a{color:inherit;text-decoration:none}
.footer nav i{font-style:normal;margin:0 24px}
.footer hr{position:absolute;left:111px;width:978px;border:0;border-top:1px solid #777}
.footer h3{position:absolute;top:137px;width:1200px;text-align:center;font-size:21px;font-weight:700}
.contact{position:absolute;top:190px;display:flex;gap:12px;align-items:flex-start}
.contact .label{font-size:18px;margin-bottom:4px}
.contact .val{font-size:14px}
.contact .val.big{font-size:17px;font-weight:700}
.social{position:absolute;left:111px;top:313px;display:flex;gap:12px}
.social span{width:10px;height:10px;background:var(--white)}
.copy{position:absolute;right:110px;top:311px;font-size:14px}
</style>
</head>
<body>

<div class="topbar">
  <div class="mail">
    <svg width="14" height="11" viewBox="0 0 14 11"><rect width="14" height="11" rx="1" fill="#fff"/><path d="M0 1l7 5 7-5" stroke="#7ea6d3" fill="none" stroke-width="1.4"/></svg>
    Mail us: elaine@whitmoretalentpartners.com
  </div>
  <div class="call">
    <svg width="13" height="13" viewBox="0 0 24 24"><path fill="#fff" d="M6.6 10.8a15 15 0 0 0 6.6 6.6l2.2-2.2a1 1 0 0 1 1-.25 11.4 11.4 0 0 0 3.6.57 1 1 0 0 1 1 1V20a1 1 0 0 1-1 1A17 17 0 0 1 3 4a1 1 0 0 1 1-1h3.5a1 1 0 0 1 1 1c0 1.25.2 2.45.57 3.57a1 1 0 0 1-.25 1z"/></svg>
    Call us Today : <b>555 010 2048</b>
  </div>
</div>

<header class="header">
  <div class="brand">
    <span class="mark"></span>
    <span class="name">Whitmore<br>Talent<br>Partners</span>
  </div>
  <nav class="nav">
    <a class="active" href="#">HOME</a>
    <a href="#">ABOUT US</a>
    <a href="#">SERVICES</a>
    <a href="#">BLOG</a>
    <a href="#">CONTACT US</a>
  </nav>
  <a class="btn login" href="#">LOG IN</a>
</header>

<section class="hero" role="img" aria-label="Black and white photo of four young professionals walking together outside an office building">
  <h1 class="display">WHITMORE TALENT<br>PARTNERS</h1>
  <svg class="arrow" style="left:53px" width="12" height="22" viewBox="0 0 12 22"><path d="M10 2L2 11l8 9" stroke="#fff" stroke-width="2.4" fill="none"/></svg>
  <svg class="arrow" style="left:1135px" width="12" height="22" viewBox="0 0 12 22"><path d="M2 2l8 9-8 9" stroke="#fff" stroke-width="2.4" fill="none"/></svg>
</section>

<div class="vline" style="top:672px;height:64px"></div>
<h2 class="section-title display" style="top:748px"><span class="accent">OUR</span> SERVICES</h2>
<p class="intro" style="top:808px">Sed ut perspiciatis unde omnis iste natus error sit voluptatem accusantium doloremque laudantium, totam rem aperiam, eaque ipsa quae ab illo inventore veritatis et quasi architecto</p>

<div class="vline" style="top:929px;height:461px"></div>
<div class="service" style="left:111px;top:922px">
  <h3>Human Resources</h3>
  <p>Sed ut perspiciatis unde omnis iste natus error sit voluptatem accusantium doloremque laudantium, totam rem aperiam, eaque ipsa quae ab illo inventore veritatis et quasi architecto aspernatur aut odit aut fugit, sed quia consequuntur</p>
  <a class="btn" href="#">READ MORE »</a>
</div>
<div class="photo" style="position:absolute;left:111px;top:1159px;width:438px;height:231px" role="img" aria-label="Photo of two colleagues smiling at a laptop in a meeting"></div>

<div class="photo" style="position:absolute;left:650px;top:929px;width:438px;height:231px" role="img" aria-label="Photo of a small team reviewing documents in an office"></div>
<div class="service" style="left:650px;top:1180px">
  <h3>Executive Development</h3>
  <p>Sed ut perspiciatis unde omnis iste natus error sit voluptatem accusantium doloremque laudantium, totam rem aperiam, eaque ipsa quae ab illo inventore veritatis et quasi architecto aspernatur aut odit aut fugit, sed quia consequuntur</p>
  <a class="btn" href="#">READ MORE »</a>
</div>

<section class="about">
  <div class="text">
    <h2 class="display"><span class="accent">ABOUT</span> WHITMORE<br>TALENT PARTNERS</h2>
    <p>Sed ut perspiciatis unde omnis iste natus error sit voluptatem accusantium doloremque laudantium, totam rem aperiam, eaque ipsa quae ab illo inventore veritatis et quasi architecto beatae vitae dicta sunt explicabo. Nemo enim ipsam voluptatem quia voluptas sit aspernatur aut</p>
    <a class="btn" href="#" style="padding:0 22px">VIEW MY BIO</a>
  </div>
  <div class="photo" role="img" aria-label="Photo of a presenter at a whiteboard leading a meeting"></div>
</section>

<section class="testimonial">
  <div class="photo" role="img" aria-label="Portrait photo of a smiling client in a suit"></div>
  <h2 class="display"><span class="accent">WHAT</span> PEOPLES SAY?</h2>
  <svg class="q-open" width="42" height="36" viewBox="0 0 42 36"><path fill="#7a7a7a" d="M0 36V20C0 8 6 2 16 0v7c-5 2-7 6-7 11h7v18zm24 0V20c0-12 6-18 16-20v7c-5 2-7 6-7 11h7v18z"/></svg>
  <p class="quote">Lorem ipsum dolor sit amet, consectetur adipiscing elit, sed do eiusmod tempor incididunt ut labore et dolore magna aliqua. Ut enim ad minim veniam, quis nostrud exercitation ullamco laboris nisi ut aliquip</p>
  <p class="who">- John Doe</p>
  <p class="role">Lorem ipsum dolor sit amet</p>
  <svg class="q-close" width="42" height="36" viewBox="0 0 42 36"><path fill="#7a7a7a" d="M42 0v16c0 12-6 18-16 20v-7c5-2 7-6 7-11h-7V0zM18 0v16c0 12-6 18-16 20v-7c5-2 7-6 7-11H2V0z"/></svg>
</section>
<div class="dots"><span></span><span class="on"></span><span></span></div>

<section class="cta">
  <h2>LET'S START A CONVERSATION ABOUT YOUR TALENT NEEDS.</h2>
  <a href="#">CONTACT US</a>
</section>

<footer class="footer">
  <nav><a href="#">Home</a><i>|</i><a href="#">About Us</a><i>|</i><a href="#">Services</a><i>|</i><a href="#">Blog</a><i>|</i><a href="#">Contact Us</a></nav>
  <hr style="top:106px">
  <h3>GET IN TOUCH : <span class="accent">ELAINE WHITMORE</span></h3>
  <div class="contact" style="left:111px">
    <svg width="46" height="40" viewBox="0 0 46 40"><rect x="1" y="10" width="44" height="29" fill="none" stroke="#fff" stroke-width="2"/><path d="M1 10l22 17 22-17M1 39l16-14M45 39L29 25" stroke="#fff" stroke-width="2" fill="none"/><circle cx="23" cy="9" r="7" fill="#222" stroke="#fff" stroke-width="2"/></svg>
    <div><div class="label">Mail us:</div><div class="val">elaine@whitmoretalentpartners.com</div></div>
  </div>
  <div class="contact" style="left:532px">
    <svg width="42" height="42" viewBox="0 0 42 42"><circle cx="19" cy="19" r="17" fill="none" stroke="#fff" stroke-width="1.6"/><ellipse cx="19" cy="19" rx="7" ry="17" fill="none" stroke="#fff" stroke-width="1.4"/><path d="M2 19h34M5 10h28M5 28h28" stroke="#fff" stroke-width="1.4"/><circle cx="31" cy="31" r="5" fill="#222" stroke="#fff" stroke-width="1.6"/><path d="M35 35l5 5" stroke="#fff" stroke-width="2"/></svg>
    <div><div class="label">Website :</div><div class="val">WhitmoreTalentPartners.com</div></div>
  </div>
  <div class="contact" style="left:909px">
    <svg width="42" height="42" viewBox="0 0 42 42"><circle cx="21" cy="21" r="19" fill="none" stroke="#fff" stroke-width="2"/><path fill="#fff" d="M14 12l4 4-2 3c1.5 3 4 5.5 7 7l3-2 4 4-3 3c-8-1-15-8-16-16z"/></svg>
    <div><div class="label">Call us Today :</div><div class="val big">555 010 2048</div></div>
  </div>
  <hr style="top:277px">
  <div class="social"><span></span><span></span><span></span></div>
  <p class="copy">© Copyrights 2020. All Rights Reserved | Whitmore Talent Partners</p>
</footer>

</body>
</html>
```